모루잔는 저녁이 있는 맥주점입니다.
그동안 맥주점 인식은 2차집이었으나 1차로서 저녁요리
타코, 샌드위치, 피자, 찹스테이크, 함박스테이크, 치킨으로 저녁과 함께 수제맥주와 세계맥주를 즐기는 패밀리 음식점입니다.
특히, 쌈은 타코 샌드위치와 같이 세계 모든요리에서 싸서 먹고
행복까지 싸준다는 의미로서 건강하고 행복한 세상만들기가 모루잔 비전입니다.

```html
<!DOCTYPE html>
<html lang="ko">
<head>
<meta charset="utf-8">
<title>모루잔 전단</title>
<link href="https://fonts.googleapis.com/css2?family=Noto+Sans+KR:wght@400;700;900&family=Oswald:wght@500;700&display=swap" rel="stylesheet">
<style>
  :root {
    --bg: #f1b84c;
    --wood: #2b2928;
    --wood-dark: #1c1b1a;
    --ink: #ffffff;
    --muted: #bdb8b2;
    --accent: #f5a21c;
    --accent-yellow: #f7d23a;
    --band: #6d6a67;
    --food-a: #b45a2c;
    --food-b: #e2b267;
  }
  * { margin: 0; padding: 0; box-sizing: border-box; }
  html, body { width: 1200px; height: 1200px; overflow: hidden; background: var(--bg); }
  body { font-family: "Noto Sans KR", sans-serif; color: var(--ink); }

  .flyer {
    position: absolute; left: 190px; top: 20px; width: 820px; height: 1160px;
    background: linear-gradient(100deg, var(--wood) 0%, #353230 45%, var(--wood-dark) 100%);
    overflow: hidden;
  }

  .brand { position: absolute; left: 56px; top: 70px; }
  .brand-row { display: flex; align-items: center; gap: 14px; }
  .brand-square { width: 34px; height: 34px; background: var(--ink); }
  .brand-name { font-family: "Oswald", sans-serif; font-weight: 500; font-size: 58px; letter-spacing: 2px; line-height: 1; }
  .brand-tag { font-family: "Oswald", sans-serif; font-weight: 500; font-size: 15px; letter-spacing: 2px; margin-top: 10px; color: var(--muted); }

  .food-photo {
    position: absolute; left: 420px; top: 40px; width: 370px; height: 520px;
    border-radius: 40px 40px 180px 40px;
    background: radial-gradient(circle at 45% 55%, var(--food-b) 0%, var(--food-a) 55%, #5b2e1c 100%);
  }

  .event { position: absolute; left: 56px; top: 280px; width: 360px; }
  .event-title { font-family: "Oswald", sans-serif; font-weight: 700; font-size: 58px; line-height: 1.3; color: var(--accent); letter-spacing: 1px; }
  .event-line { font-size: 19px; font-weight: 700; line-height: 1.55; }
  .event-line .big { font-size: 30px; color: var(--accent-yellow); }
  .event-line .hl { color: var(--accent); }
  .event-new { margin-top: 14px; }
  .event-new .hl { color: var(--accent-yellow); }

  .slogan-note { position: absolute; right: 30px; top: 628px; font-size: 11px; color: var(--muted); }
  .slogan-band {
    position: absolute; left: 0; top: 650px; width: 820px; height: 120px;
    background: linear-gradient(90deg, rgba(109,106,103,0.2), var(--band) 60%, #8a8682);
  }
  .slogan { position: absolute; left: 56px; top: 666px; font-size: 36px; font-weight: 900; line-height: 1.3; }

  .info { position: absolute; left: 56px; top: 790px; font-size: 15px; line-height: 1.7; }
  .info b { color: var(--accent); margin-right: 8px; }

  .beers { position: absolute; left: 30px; top: 865px; width: 770px; height: 285px; display: flex; gap: 14px; align-items: flex-end; }
  .beer { flex: 1; min-width: 0; display: flex; flex-direction: column; }
  .beer-head { border-top: 1px solid var(--muted); padding-top: 6px; display: flex; gap: 8px; align-items: baseline; margin-bottom: 10px; }
  .beer-num { font-family: "Oswald", sans-serif; font-size: 30px; font-weight: 500; }
  .beer-cap { font-size: 12px; color: var(--muted); white-space: nowrap; }
  .beer-glass { border-radius: 10px 10px 30px 30px; background: linear-gradient(180deg, #f4efe6 0%, var(--tone) 14%, var(--tone-dark) 100%); }
  .b1 { --tone: #e8a13a; --tone-dark: #b86a1a; }
  .b2 { --tone: #c96a2c; --tone-dark: #7a2e14; }
  .b3 { --tone: #7a2418; --tone-dark: #2c0c08; }
  .b4 { --tone: #f6dd7a; --tone-dark: #e3b33a; }
  .b1 .beer-glass { height: 110px; }
  .b2 .beer-glass { height: 150px; }
  .b3 .beer-glass { height: 190px; }
  .b4 .beer-glass { height: 225px; border-radius: 60px 60px 40px 40px; }
</style>
</head>
<body>
  <main class="flyer">
    <header class="brand">
      <div class="brand-row">
        <span class="brand-square"></span>
        <span class="brand-name">MORUJAN</span>
      </div>
      <p class="brand-tag">TACO · STEAK CAFE &amp; MODERN BAR</p>
    </header>

    <div class="food-photo" role="img" aria-label="샌드위치, 페퍼로니 피자, 타코, 샐러드 요리 사진"></div>

    <section class="event">
      <h2 class="event-title">EVENT</h2>
      <p class="event-line">매월 <span class="big">3일</span> 모루데이 <span class="hl">하우스생맥 1+1</span></p>
      <p class="event-line">매월 <span class="big">30일</span> 공영하시는</p>
      <p class="event-line"><span class="hl">공무원을 위한</span> 참공데이 <span class="hl">타코 1접시!</span></p>
      <p class="event-line event-new"><span class="hl">신메뉴 출시!</span></p>
      <p class="event-line">맥주와 즐기는 타코, 샌드위치,</p>
      <p class="event-line">피자, 찹스테이크</p>
    </section>

    <p class="slogan-note">모든 메뉴는 포장 가능하며 가격은 매장 상황에 따라 변동됩니다</p>
    <div class="slogan-band"></div>
    <h1 class="slogan">가족들과 즐길 수 있는<br>저녁이 있는 맥주점 모루잔</h1>

    <section class="info">
      <p><b>위치</b>경북 한빛시 중앙로 18 클로벤타워 1층</p>
      <p><b>영업시간</b>17:00~24:00 (연중무휴) <b style="margin-left:14px">전화</b>054-321-7788</p>
    </section>

    <section class="beers">
      <div class="beer b1">
        <div class="beer-head"><span class="beer-num">01</span><span class="beer-cap">부드러운 라거</span></div>
        <div class="beer-glass" role="img" aria-label="라거 맥주 잔 사진"></div>
      </div>
      <div class="beer b2">
        <div class="beer-head"><span class="beer-num">02</span><span class="beer-cap">진하고 고소한 에일</span></div>
        <div class="beer-glass" role="img" aria-label="앰버 에일 맥주 잔 사진"></div>
      </div>
      <div class="beer b3">
        <div class="beer-head"><span class="beer-num">03</span><span class="beer-cap">가족끼리 함께 즐기는</span></div>
        <div class="beer-glass" role="img" aria-label="흑맥주 잔 사진"></div>
      </div>
      <div class="beer b4">
        <div class="beer-head"><span class="beer-num">04</span><span class="beer-cap">세계맥주점 모루잔</span></div>
        <div class="beer-glass" role="img" aria-label="밀맥주 튤립 잔 사진"></div>
      </div>
    </section>
  </main>
</body>
</html>
```